RVM Flooring Flyer/Direct Mail

I need a flyer that will be distributed by letterboxing. this flyer will be offering free measure and quotes for supply and installation of timber, bamboo, and laminate flooring. The flyer will need to eye catching and professional looking.
The main purpose of the flyer is to generate appointments that will be followed up by a sales measure and quote team.

- Free Measure and Quote
Services:
- Remove and dispose of old floor coverings
- Pre installation floor repair
- New floor installation
- Free dust and clean on every new floor installation

I have some design files, logo and stock images, the flyer must not clash with the logo and business card.

You can use any image from Pextra Images as I have subscription with them.
https://images.pextrafoto.com/au/gallery

Here are the links to the Timber and Bamboo flooring supplier that I will be buying from and the third link is for the laminate flooring supplier. Note, this is for getting an idea of what products we will be supplying and installing, Do not use their images!

https://www.grainhaven.com.au/timber-flooring/
https://cantorvex.com.au/bamboo-flooring/
http://www.dalvorsurfaces.com.au/brands/tenmark-laminate/

Target Market(s)

Domestic home owners

Industry/Entity Type

Construction Company

Colors

Designer to choose colors to be used in the design.

Requirements
Must have
• Size: A6 or DL
Nice to have
• Timber: Spotted Gum, Eastern States Blackbutt, Jarrah, Marri, and a large collection of French Oak.
• Bamboo: Our Bamboo range of flooring is engineered to withstand the extremes of the Australian climate.
• Laminate: All our laminate range comes with a 25 year product warranty. Choose from a large range of patterns, colours and finishes.

```html
<!DOCTYPE html>
<html lang="en">
<head>
<meta charset="utf-8">
<title>RVM Flooring – Free Measure and Quote Flyer</title>
<link rel="stylesheet" href="https://fonts.googleapis.com/css2?family=Oswald:wght@300;500;700&family=Lato:ital,wght@0,400;0,700;0,900;1,400&family=Roboto+Condensed:ital,wght@0,400;0,700;1,400&display=swap">
<style>
  :root {
    --backdrop: #5a5a5a;
    --charcoal: #26282a;
    --charcoal-light: #3a3c3e;
    --paper: #f4f4f4;
    --ink: #2b2b2b;
    --grey-label: #8a8c8e;
    --amber: #c98a3a;
    --oak-light: #d9a24c;
    --oak-dark: #6b5a44;
    --white: #ffffff;
  }
  * { box-sizing: border-box; margin: 0; padding: 0; }
  html, body { width: 1071px; height: 1200px; overflow: hidden; }
  body {
    background: var(--backdrop);
    font-family: "Lato", sans-serif;
    position: relative;
  }
  .card {
    position: absolute;
    left: 155px;
    width: 760px;
    height: 539px;
    overflow: hidden;
    box-shadow: 0 8px 24px rgba(0,0,0,.35);
  }
  /* ---------- Front ---------- */
  .card--front { top: 38px; background: var(--charcoal); }
  .front-wood {
    position: absolute; inset: 0;
    background: linear-gradient(115deg, #1f2122 0%, #34373a 30%, #222425 55%, #3a3c3d 80%, #1e2021 100%);
  }
  .front-title {
    position: absolute; left: 26px; top: 26px;
    font-family: "Oswald", sans-serif; font-size: 40px; color: var(--white);
    letter-spacing: .5px;
  }
  .front-title .bold { font-weight: 700; }
  .front-title .light { font-weight: 300; }
  .brand {
    position: absolute; display: flex; align-items: center; gap: 8px;
    font-family: "Lato", sans-serif; font-weight: 400; letter-spacing: 2px;
    color: var(--white); text-transform: uppercase;
  }
  .brand .mark { width: 12px; height: 12px; background: var(--white); }
  .front .brand, .card--front .brand { right: 40px; top: 48px; font-size: 14px; }
  .front-photo {
    position: absolute; left: 0; right: 0; top: 102px; height: 270px;
    border-top: 3px solid var(--white);
    background: linear-gradient(180deg, #dfe2e6 0%, #c9ccd0 45%, #a88a6a 75%, #7a5d44 100%);
  }
  .about-label {
    position: absolute; left: 26px; top: 120px;
    background: var(--grey-label); color: var(--white);
    font-family: "Roboto Condensed", sans-serif; font-weight: 700; font-size: 22px;
    padding: 4px 12px;
  }
  .about-text {
    position: absolute; left: 20px; right: 20px; top: 160px;
    background: rgba(255,255,255,.55); padding: 8px 12px;
    font-size: 12.5px; line-height: 1.35; color: var(--ink);
  }
  .front-footer {
    position: absolute; left: 0; right: 0; top: 372px; bottom: 0;
  }
  .call {
    position: absolute; left: 46px; top: 26px;
    font-family: "Roboto Condensed", sans-serif; color: var(--white);
  }
  .call .label { font-weight: 700; font-size: 24px; display: block; }
  .call .phone { font-size: 26px; font-style: italic; display: block; margin-top: 2px; }
  .divider { position: absolute; left: 200px; top: 24px; width: 2px; height: 62px; background: var(--white); }
  .offer {
    position: absolute; left: 228px; top: 34px;
    font-family: "Roboto Condensed", sans-serif; font-style: italic;
    color: var(--white); font-size: 19px; line-height: 1.4;
  }
  .swatch { position: absolute; top: 20px; width: 92px; height: 72px; }
  .swatch--oak { left: 510px; background: linear-gradient(135deg, #e3b062, #c48a36); }
  .swatch--dark { left: 614px; background: linear-gradient(135deg, #8a7458, #4d3f2e); }
  /* ---------- Back ---------- */
  .card--back { top: 617px; background: var(--paper); }
  .back-planks {
    position: absolute; left: 0; top: 0; width: 760px; height: 200px;
    background: linear-gradient(100deg, #e6d8c4 0%, #cdb89b 25%, #bfa27a 45%, #a58a6a 62%, #7f6a56 80%, #4d4a47 100%);
    clip-path: polygon(0 0, 100% 0, 100% 100%, 62% 60%, 45% 10%, 30% 55%, 0 25%);
  }
  .card--back .brand { right: 46px; top: 88px; font-size: 14px; }
  .back-headline {
    position: absolute; left: 40px; top: 196px; color: var(--ink);
  }
  .back-headline .small { font-size: 17px; }
  .back-headline .big { font-weight: 900; font-size: 22px; }
  .line-one { display: block; }
  .line-two { display: block; border-bottom: 1.5px solid var(--ink); padding-bottom: 4px; }
  .ranges {
    margin-top: 8px; font-size: 13px; font-weight: 700; color: var(--amber);
    letter-spacing: .5px; display: flex; gap: 14px; padding-left: 10px;
  }
  .services { position: absolute; left: 40px; top: 330px; color: var(--ink); }
  .services h2 { font-size: 16px; font-weight: 900; margin-bottom: 8px; }
  .services ul { list-style: none; }
  .services li { font-size: 13px; line-height: 1.7; display: flex; align-items: center; gap: 10px; }
  .services li::before { content: ""; width: 7px; height: 7px; background: var(--amber); }
  .address { position: absolute; left: 440px; top: 296px; width: 260px; }
  .address .to { font-size: 13px; color: var(--ink); margin-bottom: 8px; }
  .address .rule { height: 1px; background: #555; margin-bottom: 16px; }
  .back-band { position: absolute; left: 0; right: 0; bottom: 14px; height: 26px; background: linear-gradient(90deg, #222425, #3a3c3e, #222425); }
</style>
</head>
<body>
  <section class="card card--front" aria-label="Flyer front">
    <div class="front-wood" role="img" aria-label="Dark timber planks background"></div>
    <h1 class="front-title"><span class="bold">Free</span> <span class="light">MEASURE</span> <span class="bold">and</span> <span class="light">QUOTE</span></h1>
    <div class="brand"><span class="mark"></span>RVM Flooring</div>
    <div class="front-photo" role="img" aria-label="Bright open-plan kitchen and living room with timber floor"></div>
    <div class="about-label">At RVM flooring</div>
    <p class="about-text">we specialise in prefinished timber, bamboo and laminate flooring. We strive to provide a unique and professional experience to all our customers. Our goal is to provide the highest stranded in customer service, integrity, quality and value for money. As a family business we understand the importance of relationship and seek to make your experience one you will be pleased you made.</p>
    <div class="front-footer">
      <div class="call"><span class="label">CALL TODAY</span><span class="phone">08 9000 4817</span></div>
      <div class="divider"></div>
      <p class="offer">For your obligations free quote<br>To view our range of products</p>
      <div class="swatch swatch--oak" role="img" aria-label="Light oak floor sample"></div>
      <div class="swatch swatch--dark" role="img" aria-label="Dark timber floor sample"></div>
    </div>
  </section>

  <section class="card card--back" aria-label="Flyer back">
    <div class="back-planks" role="img" aria-label="Fan of timber, bamboo and laminate floor planks"></div>
    <div class="brand"><span class="mark"></span>RVM Flooring</div>
    <div class="back-headline">
      <span class="line-one"><span class="small">Specialising in </span><span class="big">SUPPLY</span><span class="small"> and</span></span>
      <span class="line-two"><span class="big">INSTALLATION</span><span class="small"> of Prefinished</span></span>
      <div class="ranges"><span>LAMINATE</span><span>•</span><span>BAMBOO</span><span>•</span><span>HARDWOOD</span></div>
    </div>
    <div class="services">
      <h2>SERVICES:</h2>
      <ul>
        <li>Remove and dispose of old floor coverings</li>
        <li>Pre installation floor repair</li>
        <li>New floor installation</li>
        <li>Free dust and clean on every new floor installation</li>
      </ul>
    </div>
    <div class="address">
      <p class="to">To,</p>
      <div class="rule"></div>
      <div class="rule"></div>
      <div class="rule"></div>
      <div class="rule"></div>
    </div>
    <div class="back-band" role="img" aria-label="Dark timber strip"></div>
  </section>
</body>
</html>
```